Stationary for Keeping Steady

we are in the process of creating a more professional image for our company Keeping Steady Paramedical Services. We have recently had a new logo and general brochure designed using artpitchhub and have been impressed by the quality of submissions.

We need:
- Letterhead (A4)
- Business Cards
- With compliments slips
- Email stationary

Letterhead information:
Address - 47 Wattlebrook Drive, Fernhollow Vic 3091
Phone - 1800 462 817
email - enquiries@keepsteady.com.au
Internet - www.keepsteady.com.au
ABN - 82 463 915 207
ACN - 264 871 035

Files need to be able to be edited in Illustrator CS2

Business Cards / with compliments slips / email stationary:
Double sided.
One side to have Name, Mobile number, company phone 1800462817, email, internet address

Files need to be able to be edited in Illustrator CS2 (except email stationary)

Our website is www.keepsteady.com.au for more information. Do not base designs on the website as it will eventually be revised.

Target Market(s)

Australian based businesses, government departments and schools. We specialise in corporate customers rather than public first aid course

Industry/Entity Type

Internet

Requirements
Must have
• Where applicable file to be editable in illustrator CS2 to allow future alterations.

```html
<!DOCTYPE html>
<html lang="en">
<head>
<meta charset="utf-8">
<title>Keeping Steady – Business Cards</title>
<link rel="stylesheet" href="https://fonts.googleapis.com/css2?family=Questrial&family=Mulish:wght@700&display=swap">
<style>
  :root {
    --backdrop: #d8cfca;
    --card-top: #ffffff;
    --card-bottom: #e6e7e8;
    --brand-red: #c8202e;
    --brand-black: #111111;
    --ink: #1a1a1a;
    --card-edge: #8a8484;
  }
  * { margin: 0; padding: 0; box-sizing: border-box; }
  html, body { width: 1200px; height: 900px; overflow: hidden; }
  body {
    background: var(--backdrop);
    font-family: "Questrial", "Century Gothic", sans-serif;
    color: var(--ink);
    position: relative;
  }
  .card {
    position: absolute;
    top: 295px;
    width: 482px;
    height: 310px;
    border-radius: 14px;
    overflow: hidden;
    background: linear-gradient(180deg, var(--card-top) 0%, var(--card-bottom) 100%);
    box-shadow: 0 0 0 1px var(--card-edge), 0 3px 8px rgba(0,0,0,0.18);
  }
  .card--front { left: 86px; }
  .card--back { left: 634px; }

  .brand {
    position: absolute;
    display: flex;
    align-items: center;
    gap: 10px;
  }
  .brand__square {
    width: 36px; height: 36px;
    background: var(--brand-red);
    flex: none;
  }
  .brand__name { line-height: 1; white-space: nowrap; }
  .brand__name span { display: block; }
  .brand__title { color: var(--brand-red); }
  .brand__sub { color: var(--ink); }

  .card--front .brand { left: 30px; top: 24px; }
  .card--front .brand__title { font-size: 24px; }
  .card--front .brand__sub { font-size: 11.5px; margin-top: 3px; }

  .holder {
    position: absolute;
    left: 30px; top: 98px;
    font-family: "Mulish", "Century Gothic", sans-serif;
    font-weight: 700;
    font-size: 21px;
    color: var(--brand-black);
  }
  .details {
    position: absolute;
    left: 30px; top: 143px;
    font-size: 14.5px;
    line-height: 18px;
    list-style: none;
  }
  .details li { display: flex; align-items: center; gap: 3px; }
  .details .icon { width: 14px; height: 12px; margin-left: -3px; flex: none; }
  .details .gap { margin-top: 18px; }

  .edge-band {
    position: absolute;
    top: 0; bottom: 0;
  }
  .card--front .edge-band {
    right: 0; width: 38px;
    background: linear-gradient(180deg, var(--brand-red) 0 62%, var(--brand-black) 62% 100%);
  }
  .card--back .edge-band {
    left: 0; width: 62px;
    background: linear-gradient(180deg, var(--brand-red) 0 22%, var(--brand-black) 22% 100%);
  }

  .card--back .brand { left: 193px; top: 132px; }
  .card--back .brand__title { font-size: 31px; }
  .card--back .brand__sub { font-size: 16px; margin-top: 5px; }
</style>
</head>
<body>

<section class="card card--front" aria-label="Business card front">
  <div class="brand">
    <div class="brand__square"></div>
    <div class="brand__name">
      <span class="brand__title">Keeping Steady</span>
      <span class="brand__sub">Paramedical Services Pty Ltd</span>
    </div>
  </div>

  <h1 class="holder">Sam Taylor</h1>

  <ul class="details">
    <li>47 Wattlebrook Drive,</li>
    <li>Fernhollow Vic 3091</li>
    <li>
      <svg class="icon" viewBox="0 0 14 12" aria-hidden="true"><path fill="#c8202e" d="M1 4c0-2 3-3 6-3s6 1 6 3v1h-3V4H4v1H1z M3 6h8l1 5H2z"/></svg>
      1800 462 817
    </li>
    <li>
      <svg class="icon" viewBox="0 0 14 12" aria-hidden="true"><rect x="4" y="0" width="6" height="12" rx="1" fill="#c8202e"/><rect x="5" y="2" width="4" height="4" fill="#fff"/></svg>
      234 61827 509
    </li>
    <li>
      <svg class="icon" viewBox="0 0 14 12" aria-hidden="true"><rect x="1" y="2" width="12" height="8" fill="none" stroke="#c8202e" stroke-width="1.4"/><path d="M1 2l6 5 6-5" fill="none" stroke="#c8202e" stroke-width="1.4"/></svg>
      enquiries@keepsteady.com.au
    </li>
    <li class="gap">ABN - 82 463 915 207</li>
    <li>ACN - 264 871 035</li>
  </ul>

  <div class="edge-band"></div>
</section>

<section class="card card--back" aria-label="Business card back">
  <div class="edge-band"></div>
  <div class="brand">
    <div class="brand__name">
      <span class="brand__title">Keeping Steady</span>
      <span class="brand__sub">Paramedical Services Pty Ltd</span>
    </div>
  </div>
</section>

</body>
</html>
```